Modern Minimalistic Supplement Label

Opportunity for recurring projects with a growing company. We have provided a detailed creative brief and all necessary files and guidelines. If you have any questions we will be closely monitoring the discussion board and email provided.

THE NAMES LISTED IN THE BRIEF ARE DIFFERENT FROM THE LABEL TEMPLATES. This is a private label brand. The label templates given are generic so please examine the entire brief before starting.

Use the PSD mockups attached and pair the labels with the correct bottles.

Do not use an entirely white background.

This could be excellent portfolio material.

Start by looking at the "CREATIVE_BRIEF" file. Logo files are contained in the "67046451" zip file.

UPDATE* Use the following business address for the "manufactured for" box on the labels.

Bramwell
4817 Pelton Ave. #2096
Ann Arbor MI 48276

Target Market(s)

All information provided in "CREATIVE_BRIEF" file.

Industry/Entity Type

Supplement

Requirements
Must have
• All information provided in "CREATIVE_BRIEF" file.
Nice to have
Should not have

```html
<!DOCTYPE html>
<html lang="en">
<head>
<meta charset="UTF-8">
<title>Bramwell Whey Protein Isolate Blend Label</title>
<link href="https://fonts.googleapis.com/css2?family=Oswald:wght@400;500&family=Space+Mono&display=swap" rel="stylesheet">
<style>
  :root {
    --page-bg: #ecedee;
    --label-bg: #fbfbfb;
    --ink: #3b3b3d;
    --ink-soft: #555558;
    --rule: #9a9a9c;
    --ridge-light: #f4f4f5;
    --ridge-mid: #e3e4e6;
    --band-dark: #7d7e80;
    --band-light: #dcdddf;
    --flavor: #f4a623;
    --on-band: #ffffff;
  }
  * { margin: 0; padding: 0; box-sizing: border-box; }
  html, body {
    width: 1200px;
    height: 1200px;
    overflow: hidden;
    background: var(--page-bg);
  }
  .label {
    position: absolute;
    left: 100px;
    top: 170px;
    width: 1000px;
    height: 860px;
    background: var(--label-bg);
    box-shadow: 0 2px 14px rgba(0,0,0,0.08);
    overflow: hidden;
  }
  .ridge-backdrop {
    position: absolute;
    left: 0;
    top: 300px;
    width: 1000px;
    height: 340px;
    background: linear-gradient(180deg, var(--label-bg) 0%, var(--ridge-light) 40%, var(--ridge-mid) 100%);
    opacity: 0.85;
  }
  .brand {
    position: absolute;
    top: 92px;
    left: 0;
    width: 100%;
    display: flex;
    align-items: center;
    justify-content: center;
    gap: 16px;
  }
  .brand-mark {
    width: 22px;
    height: 22px;
    background: var(--ink);
  }
  .brand-name {
    font-family: 'Oswald', sans-serif;
    font-weight: 400;
    font-size: 44px;
    letter-spacing: 6px;
    color: var(--ink);
    line-height: 1;
  }
  .product-title {
    position: absolute;
    left: 150px;
    top: 228px;
    font-family: 'Oswald', sans-serif;
    color: var(--ink);
    text-transform: uppercase;
    line-height: 1;
  }
  .title-whey {
    display: block;
    font-size: 92px;
    font-weight: 500;
  }
  .title-protein {
    display: block;
    font-size: 168px;
    font-weight: 500;
    margin-top: 2px;
    letter-spacing: 1px;
  }
  .title-isolate {
    display: block;
    font-size: 58px;
    font-weight: 400;
    margin-top: 8px;
  }
  .claims {
    position: absolute;
    left: 150px;
    top: 650px;
    font-family: 'Space Mono', monospace;
    color: var(--ink-soft);
  }
  .claims-rule {
    width: 100px;
    height: 2px;
    background: var(--rule);
    margin-bottom: 18px;
  }
  .claim-protein {
    font-size: 20px;
    letter-spacing: 1px;
  }
  .claim-protein strong {
    font-family: 'Oswald', sans-serif;
    font-weight: 500;
    font-size: 32px;
    color: var(--ink);
  }
  .claim-benefit {
    font-size: 19px;
    letter-spacing: 1px;
    margin-top: 12px;
  }
  .info-band {
    position: absolute;
    left: 0;
    bottom: 0;
    width: 100%;
    height: 96px;
    display: flex;
  }
  .info-band-facts {
    flex: 1;
    background: linear-gradient(90deg, var(--band-dark) 0%, var(--band-dark) 35%, var(--band-light) 100%);
    padding: 22px 0 0 40px;
    font-family: 'Space Mono', monospace;
    font-size: 17px;
    line-height: 1.4;
    color: var(--on-band);
    letter-spacing: 0.5px;
  }
  .info-band-flavor {
    width: 340px;
    background: var(--flavor);
    display: flex;
    align-items: center;
    padding-left: 40px;
    font-family: 'Space Mono', monospace;
    font-size: 21px;
    color: var(--on-band);
    letter-spacing: 0.5px;
  }
</style>
</head>
<body>
  <div class="label">
    <div class="ridge-backdrop" role="img" aria-label="Faint pale grey mountain ridge backdrop behind the product name"></div>

    <div class="brand">
      <span class="brand-mark"></span>
      <span class="brand-name">BRAMWELL</span>
    </div>

    <h1 class="product-title">
      <span class="title-whey">Whey</span>
      <span class="title-protein">Protein</span>
      <span class="title-isolate">Isolate Blend</span>
    </h1>

    <div class="claims">
      <div class="claims-rule"></div>
      <p class="claim-protein"><strong>24g</strong> PROTEIN</p>
      <p class="claim-benefit">FOR INCREASED MUSCULAR RECOVERY</p>
    </div>

    <div class="info-band">
      <div class="info-band-facts">
        <p>NET WT. 907 G (2 LB)</p>
        <p>DIETARY SUPPLEMENT</p>
      </div>
      <div class="info-band-flavor">CHOCOLATE FLAVOR</div>
    </div>
  </div>
</body>
</html>
```